Re-design of current business cards

We are updating our website with new colors and layout. Would like to re-design our business cards to co-ordinate. See attached pdf with new Brindlecraft website colors. We would also like to combine our 2 brands on the one business card. Attached is the new design for our Brindlecraft website, current business cards, which are one sided, brindlecraft logo in tiff, .ai for fonts. Brindlecraft logo font is Optimum, Quillmarsh website home page image, Quillmarsh brand statics for products which includes the logo for this brand.

Quillmarsh brand will stay the dark gray on the website. See attached statics for product and website home page.
Updates

The business cards will be 2 sided. Brindlecraft Brand on one side and Quillmarsh Brand on the other. The colors for Brindlecraft need to follow the color scheme of the brindlecraft website pdf I uploaded. The colors are a blue, lighter teal blue and white. Quillmarsh needs to follow the dark gray color on files uploaded

Target Market(s)

The trade and consumers

Industry/Entity Type

Home Furnishing

Contact Information for Business Card

We are updating our website with new colors and layout. Would like to re-design our business cards to co-ordinate. We would also like to combine our 2 brands onto 1 2 sided business cards.

Requirements
Must have
• Colors that match our new website, see attached image.
• RGB colors
• navy -#152842
• teal - 98aeb9
• The gray color used for Quillmarsh brands.
• ll logos and fonts should stay the same.

```html
<!DOCTYPE html>
<html lang="en">
<head>
<meta charset="utf-8">
<title>Brindlecraft &amp; Quillmarsh Business Cards</title>
<link href="https://fonts.googleapis.com/css2?family=Cormorant+Garamond:wght@400;500&family=Tenor+Sans&display=swap" rel="stylesheet">
<style>
  :root {
    --bg: #d6d6d6;
    --navy: #152842;
    --teal: #98aeb9;
    --white: #ffffff;
    --soft-white: #d9e1e8;
    --gray-light: #a9a9a9;
    --gray-text: #b9b9b9;
  }
  * { margin: 0; padding: 0; box-sizing: border-box; }
  html, body { width: 1200px; height: 563px; overflow: hidden; }
  body {
    background: var(--bg);
    position: relative;
    font-family: "Tenor Sans", sans-serif;
  }
  .card { position: absolute; overflow: hidden; }

  /* Brindlecraft side */
  .card-brindlecraft {
    left: 110px; top: 154px; width: 418px; height: 238px;
    background: var(--white);
    border-radius: 6px;
  }
  .web-band {
    position: absolute; left: 0; top: 0; width: 100%; height: 19px;
    background: linear-gradient(90deg, #8ea4b0, var(--teal) 60%, #aebfc8);
    color: var(--navy);
    font-size: 11px; letter-spacing: 7.6px;
    line-height: 19px; padding-left: 18px; white-space: nowrap;
  }
  .texture-fade {
    position: absolute; left: 0; top: 19px; width: 160px; height: 120px;
    background: radial-gradient(ellipse at 0% 20%, #e4e6e9 0%, #f1f2f4 45%, rgba(255,255,255,0) 75%);
  }
  .brand-mark {
    position: absolute; right: 10px; top: 60px;
    display: flex; align-items: center; gap: 8px;
  }
  .brand-dot {
    width: 48px; height: 48px; border-radius: 50%;
    background: var(--teal);
  }
  .brand-name {
    font-size: 15px; color: var(--navy); letter-spacing: 0.3px; white-space: nowrap;
  }
  .person-name {
    position: absolute; left: 18px; top: 126px;
    font-size: 22px; font-weight: 400; color: var(--navy); letter-spacing: 0.2px;
  }
  .person-title {
    position: absolute; left: 19px; top: 153px;
    font-size: 9px; color: var(--navy);
  }
  .info-band {
    position: absolute; left: 0; top: 167px; width: 100%; height: 71px;
    background: linear-gradient(180deg, #1c3455, var(--navy));
    color: var(--soft-white);
  }
  .contact-list { position: absolute; left: 20px; top: 6px; list-style: none; }
  .contact-list li {
    display: flex; align-items: center; gap: 8px;
    font-size: 11px; line-height: 15px;
  }
  .contact-list svg { width: 11px; height: 11px; }
  .address {
    position: absolute; right: 10px; top: 6px; text-align: right;
    font-size: 11px; line-height: 15px; font-style: normal;
  }
  .rule {
    position: absolute; left: 18px; right: 8px; top: 58px; height: 1px;
    background: var(--soft-white);
  }

  /* Quillmarsh side */
  .card-quillmarsh {
    left: 638px; top: 153px; width: 432px; height: 239px;
    border-radius: 8px;
    background: radial-gradient(ellipse at 40% 30%, #8f8f8f 0%, #7a7a7a 45%, #666 100%);
  }
  .header-panel {
    position: absolute; left: 0; top: 0; width: 100%; height: 62px;
    background: linear-gradient(180deg, #999, #8c8c8c);
  }
  .header-rule {
    position: absolute; left: 0; top: 65px; width: 100%; height: 3px;
    background: var(--gray-light);
  }
  .wordmark {
    position: absolute; left: 10px; top: 8px;
    font-family: "Cormorant Garamond", serif; font-weight: 500;
    font-size: 50px; line-height: 1; color: var(--white); letter-spacing: -1.5px;
    white-space: nowrap;
  }
  .endorsement {
    position: absolute; right: 16px; top: 39px;
    font-size: 10px; color: var(--white); white-space: nowrap;
  }
  .tagline {
    position: absolute; left: 14px; top: 78px;
    font-size: 23px; color: var(--gray-text);
  }
  .q-details {
    position: absolute; right: 16px; top: 123px; text-align: right;
    list-style: none; color: var(--white); font-size: 11px;
  }
  .q-details li {
    height: 20.3px; display: flex; justify-content: flex-end; align-items: center; gap: 7px;
  }
  .q-details svg { width: 9px; height: 9px; }
  .q-name {
    position: absolute; left: 13px; top: 181px;
    font-size: 24px; font-weight: 400; color: var(--white);
  }
  .q-title {
    position: absolute; left: 14px; top: 208px;
    font-size: 9px; color: #d0d0d0;
  }
</style>
</head>
<body>

<section class="card card-brindlecraft" aria-label="Brindlecraft business card">
  <div class="web-band">www.brindlecraft.com</div>
  <div class="texture-fade" role="img" aria-label="Soft fading square-dot texture"></div>
  <div class="brand-mark">
    <span class="brand-dot"></span>
    <span class="brand-name">BRINDLECRAFT</span>
  </div>
  <h1 class="person-name">MAREN DALTON</h1>
  <p class="person-title">GRAPHICS/PHOTOGRAPHY DIRECTOR</p>
  <div class="info-band">
    <ul class="contact-list">
      <li><svg viewBox="0 0 12 12"><circle cx="6" cy="6" r="6" fill="#d9e1e8"/><path d="M3 5c0-1 1.3-1.8 3-1.8S9 4 9 5H7.6V4.6H4.4V5zM4 6h4l.7 2.5H3.3z" fill="#152842"/></svg>555.201.4830</li>
      <li><svg viewBox="0 0 12 12"><rect width="12" height="12" rx="2" fill="#d9e1e8"/><rect x="3" y="2.5" width="6" height="7" fill="#152842"/><rect x="4" y="3.5" width="4" height="1.5" fill="#d9e1e8"/></svg>555.201.4857</li>
      <li><svg viewBox="0 0 12 12"><circle cx="6" cy="6" r="6" fill="#d9e1e8"/><rect x="3" y="4" width="6" height="4.2" fill="#152842"/><path d="M3 4l3 2.3L9 4" stroke="#d9e1e8" stroke-width=".7" fill="none"/></svg>mdalton@brindlecraft.com</li>
    </ul>
    <address class="address">PO BOX 214/1870 CEDAR BEND RD<br>MAPLE FALLS, VERMONT 05730</address>
    <div class="rule"></div>
  </div>
</section>

<section class="card card-quillmarsh" aria-label="Quillmarsh business card">
  <div class="header-panel"></div>
  <div class="header-rule"></div>
  <div class="wordmark">QUILLMARSH</div>
  <div class="endorsement">by BRINDLECRAFT</div>
  <p class="tagline">Discover the luxury of home.</p>
  <ul class="q-details">
    <li>PO BOX 214/1870 CEDAR BEND RD</li>
    <li>MAPLE FALLS, VERMONT 05730</li>
    <li><svg viewBox="0 0 10 10"><circle cx="5" cy="5" r="4.3" fill="none" stroke="#fff" stroke-width="1"/><path d="M3 5.2c0-.9.9-1.5 2-1.5s2 .6 2 1.5z" fill="#fff"/></svg>555.201.4830</li>
    <li><svg viewBox="0 0 10 10"><circle cx="5" cy="5" r="4.3" fill="none" stroke="#fff" stroke-width="1"/><rect x="3.4" y="3" width="3.2" height="4" fill="#fff"/></svg>555.201.4857</li>
    <li><svg viewBox="0 0 10 10"><circle cx="5" cy="5" r="4.3" fill="none" stroke="#fff" stroke-width="1"/><rect x="3" y="3.6" width="4" height="2.8" fill="#fff"/></svg>mdalton@brindlecraft.com</li>
  </ul>
  <h2 class="q-name">MAREN DALTON</h2>
  <p class="q-title">GRAPHICS/PHOTOGRAPHY DIRECTOR</p>
</section>

</body>
</html>
```